Logo/ Web site and business cards for my wardrobe consulting businsess.
I am a fashion stylist and am looking to create a website to promote my styling services. I want the website to contain my portfolio as well as testimonials. I want it to be live containing the feeds of all of my social networks.The website should be clean modern and fashionable.
I have invisioned the logo to have two over lapping hangers with the words velvet closets written in cursive at the bottom of each hanger. Id like for the logo to be stylish and strong.
The business card should be simple containing the logo my name Marlene Ostrova and web adress.
Target Market(s)
20-65 women
Industry/Entity Type
Fashion
Logo Text
Velvet Closets
Look and feel
Each slider illustrates characteristics of the customer's brand and the style your logo design should communicate.

```html
<!DOCTYPE html>
<html lang="en">
<head>
<meta charset="utf-8">
<title>Velvet Closets — Services</title>
<link href="https://fonts.googleapis.com/css2?family=Arvo:wght@400;700&family=Arimo:wght@400;700&display=swap" rel="stylesheet">
<style>
  :root {
    --ink: #000000;
    --paper: #ffffff;
    --text: #2b2b2b;
    --nav-text: #ffffff;
    --nav-active: #f2cf6b;
    --frame: #222222;
    --rule: #111111;
    --social-blue: #3b5a9a;
    --social-azure: #2a6fc4;
    --social-brown: #8a6a50;
    --social-light: #e6e6e6;
  }
  * { margin: 0; padding: 0; box-sizing: border-box; }
  html, body { width: 1129px; height: 1200px; overflow: hidden; background: var(--paper); }
  body { position: relative; font-family: "Arimo", Arial, sans-serif; color: var(--text); }

  .site-header { position: absolute; left: 0; top: 0; width: 1129px; height: 140px; background: var(--ink); }
  .brand { position: absolute; left: 69px; top: 78px; font-family: "Arvo", serif; font-size: 16px; color: var(--nav-text); letter-spacing: 0.3px; }
  .main-nav a { position: absolute; top: 62px; transform: translateX(-50%); font-family: "Arvo", serif; font-weight: 700; font-size: 12px; color: var(--nav-text); text-decoration: none; text-transform: uppercase; letter-spacing: 0.2px; }
  .main-nav a.is-active { color: var(--nav-active); }
  .main-nav a.is-active::after { content: ""; position: absolute; left: -10px; right: -10px; top: 28px; height: 2px; background: #cfcfcf; }

  .page-title { position: absolute; left: 155px; top: 150px; width: 805px; font-family: "Arvo", serif; font-weight: 400; font-size: 38px; color: var(--ink); border-bottom: 2px solid var(--rule); padding-bottom: 4px; line-height: 46px; }

  .gallery-photo { position: absolute; border: 2px solid var(--frame); }
  .photo-rack { left: 158px; top: 241px; width: 267px; height: 223px; background: linear-gradient(160deg, #f2f0ee, #c9c3bd 70%, #8a827c); }
  .photo-lounge { left: 434px; top: 241px; width: 280px; height: 223px; background: linear-gradient(180deg, #f4f2f0, #d8d4d0 60%, #9a8e84); }
  .photo-closet { left: 725px; top: 243px; width: 238px; height: 221px; background: linear-gradient(180deg, #f4f4f4 20%, #b9a9a0 50%, #e9e9e9 90%); }
  .gallery-arrow { position: absolute; top: 336px; }
  .arrow-prev { left: 66px; }
  .arrow-next { left: 1036px; }

  .services-copy { position: absolute; left: 158px; top: 508px; width: 800px; font-size: 20px; line-height: 25px; }
  .service-list { list-style: none; margin: 24px 0 24px; }
  .service-list li { font-weight: 700; position: relative; padding-left: 12px; }
  .service-list li svg { position: absolute; left: -6px; top: 2px; }

  .site-footer { position: absolute; left: 0; top: 1060px; width: 1129px; height: 140px; background: var(--ink); }
  .social-link { position: absolute; top: 49px; width: 43px; height: 43px; display: block; }
  .social-one { left: 778px; background: var(--social-blue); }
  .social-two { left: 860px; background: var(--social-azure); }
  .social-three { left: 947px; background: var(--social-brown); }
  .social-four { left: 1035px; background: var(--social-light); }
</style>
</head>
<body>
  <header class="site-header">
    <div class="brand">Velvet Closets</div>
    <nav class="main-nav">
      <a href="#" style="left:349px">Home</a>
      <a href="#" class="is-active" style="left:492px">Services</a>
      <a href="#" style="left:645px">About</a>
      <a href="#" style="left:834px">Testimonials</a>
      <a href="#" style="left:1013px">Contacts</a>
    </nav>
  </header>

  <h1 class="page-title">Services</h1>

  <svg class="gallery-arrow arrow-prev" width="28" height="34" viewBox="0 0 28 34"><path d="M0 17 L28 0 L18 17 L28 34 Z" fill="#000"/></svg>
  <div class="gallery-photo photo-rack" role="img" aria-label="Clothing rack with dresses, bags and shoes beside a dress form"></div>
  <div class="gallery-photo photo-lounge" role="img" aria-label="Tufted grey chair with a leather bag in front of a white mirror"></div>
  <div class="gallery-photo photo-closet" role="img" aria-label="Open closet rail of colourful garments under a shelf"></div>
  <svg class="gallery-arrow arrow-next" width="28" height="34" viewBox="0 0 28 34"><path d="M28 17 L0 0 L10 17 L0 34 Z" fill="#000"/></svg>

  <section class="services-copy">
    <p>Vestibulum aliquam, eros a posuere scelerisque, lacus nunc tincidunt ligula, sed vulpu-tate orci dolor sit amet lorem. Donec tincidunt vehicula facilisis. Praesent et viverra nulla, vel ullamcorper lacus. Sed blandit orci nisi, vitae ultrices ante porta eu.</p>
    <ul class="service-list">
      <li><svg width="12" height="14" viewBox="0 0 12 14"><path d="M2 2 L6 1 L5 4 L9 12 M3 5 L7 3" stroke="#333" stroke-width="1.4" fill="none"/></svg>Praesent scelerisque vehicula odio ut ultricies.</li>
      <li><svg width="12" height="14" viewBox="0 0 12 14"><path d="M2 2 L6 1 L5 4 L9 12 M3 5 L7 3" stroke="#333" stroke-width="1.4" fill="none"/></svg>Praesent scelerisque vehicula odio ut ultricies.</li>
      <li><svg width="12" height="14" viewBox="0 0 12 14"><path d="M2 2 L6 1 L5 4 L9 12 M3 5 L7 3" stroke="#333" stroke-width="1.4" fill="none"/></svg>Praesent scelerisque vehicula odio ut ultricies.</li>
      <li><svg width="12" height="14" viewBox="0 0 12 14"><path d="M2 2 L6 1 L5 4 L9 12 M3 5 L7 3" stroke="#333" stroke-width="1.4" fill="none"/></svg>Praesent scelerisque vehicula odio ut ultricies.</li>
      <li><svg width="12" height="14" viewBox="0 0 12 14"><path d="M2 2 L6 1 L5 4 L9 12 M3 5 L7 3" stroke="#333" stroke-width="1.4" fill="none"/></svg>Praesent scelerisque vehicula odio ut ultricies.</li>
    </ul>
    <p>Donec mattis libero at nisl commodo, sit amet facilisis eros auctor. Vestibulum nec laoreet nunc. Morbi at congue libero. Duis condimentum augue eu condimentum mattis. Aenean dignissim auctor egestas.</p>
  </section>

  <footer class="site-footer">
    <a href="#" class="social-link social-one" aria-label="Social network link"></a>
    <a href="#" class="social-link social-two" aria-label="Social network link"></a>
    <a href="#" class="social-link social-three" aria-label="Photo sharing link"></a>
    <a href="#" class="social-link social-four" aria-label="Booking link"></a>
  </footer>
</body>
</html>
```